Organic skincare label - minimalist, earthy, luxe design needed!

I need a label design for a luxury natural skin care line called "Velka Botaniq". Velka means 'earth' in Swahili. I would like the design to embody an earthy feel but be minimalistic and give a luxe vibe. My first product will be a Saffron and Moringa Polish.

The size of the jar is 8oz, label dimensions should be (1.625" Tall x 8.5" Wide)
I will be making other products too such as; oils + toners so I feel free to do labels for glass bottles and/or spray bottles as well.

Forest green, light pinks/nudes/beige, grey, white, gold, are colors that can be used (not all have to be used).

I have included pictures of some things I've worked on myself as well as my original logo design but I need to simplify the logo, no circle around it.
Feel free to get creative.

Thank you! :)
Updates

Target Market(s)

Socially Conscious, Beauty Enthusiast, Minimalist

Industry/Entity Type

Skin Care

Font styles to use
Sans Serif
Other font styles liked:
• "Wonderlove doodle" is the font used for "Velka" in the logo. Feel free to use that or change it as you see fit.

Requirements
Must have
• Simplistic design
would like to stick to a font close to the ones in the logo. Either the one used for the name "Velka" OR the one that the slogan "earth's elixirs" uses.

I have also included some pictures to capture the aesthetic of my social media and website.

Gender neutral

```html
<!DOCTYPE html>
<html lang="en">
<head>
<meta charset="UTF-8">
<title>Velka Botaniq – Saffron + Moringa Polish Label</title>
<link href="https://fonts.googleapis.com/css2?family=Josefin+Sans:wght@300;600;700&family=Source+Sans+3:wght@400;500&display=swap" rel="stylesheet">
<style>
  :root {
    --backdrop: #eff0f2;
    --label-white: #fbfbfc;
    --ink: #34373a;
    --ink-soft: #4a4d50;
    --nude: #ecdcd1;
    --nude-light: #f4e9e2;
    --rule: #3a3d40;
  }
  * { margin: 0; padding: 0; box-sizing: border-box; }
  html, body {
    width: 1200px;
    height: 800px;
    overflow: hidden;
    background: var(--backdrop);
  }
  .canvas {
    position: relative;
    width: 1200px;
    height: 800px;
  }
  .label {
    position: absolute;
    left: 220px;
    top: 130px;
    width: 760px;
    height: 540px;
    background: var(--label-white);
    box-shadow: 0 1px 3px rgba(0,0,0,0.06);
    overflow: hidden;
  }
  .label__texture {
    position: absolute;
    left: 0;
    bottom: 0;
    width: 100%;
    height: 175px;
    background: linear-gradient(100deg, var(--nude) 0%, var(--nude-light) 35%, var(--nude) 60%, var(--nude-light) 85%, var(--nude) 100%);
  }
  .label__content {
    position: relative;
    height: 100%;
    display: flex;
    flex-direction: column;
    align-items: center;
    text-align: center;
    color: var(--ink);
  }
  .brand-name {
    margin-top: 132px;
    font-family: "Josefin Sans", sans-serif;
    font-weight: 600;
    font-size: 46px;
    letter-spacing: 0.02em;
    color: var(--ink);
  }
  .product-name {
    margin-top: 40px;
    font-family: "Josefin Sans", sans-serif;
    font-weight: 700;
    font-size: 38px;
    letter-spacing: 0.13em;
  }
  .product-rule {
    width: 660px;
    height: 2px;
    margin-top: 10px;
    background: var(--rule);
  }
  .product-type {
    margin-top: 10px;
    font-family: "Josefin Sans", sans-serif;
    font-weight: 300;
    font-size: 30px;
    letter-spacing: 0.16em;
    color: var(--ink-soft);
  }
  .origin {
    margin-top: 26px;
    font-family: "Source Sans 3", sans-serif;
    font-weight: 500;
    font-size: 18px;
    letter-spacing: 0.04em;
    color: var(--ink-soft);
  }
  .net-volume {
    margin-top: auto;
    margin-bottom: 42px;
    font-family: "Source Sans 3", sans-serif;
    font-weight: 400;
    font-size: 14px;
    letter-spacing: 0.03em;
    color: var(--ink-soft);
  }
</style>
</head>
<body>
  <div class="canvas">
    <section class="label">
      <div class="label__texture" role="img" aria-label="Soft nude marbled stone texture band"></div>
      <div class="label__content">
        <h1 class="brand-name">Velka Botaniq</h1>
        <h2 class="product-name">SAFFRON + MORINGA</h2>
        <div class="product-rule"></div>
        <p class="product-type">POLISH</p>
        <p class="origin">MADE IN THIS COUNTRY</p>
        <p class="net-volume">8 oz / 236.58 ml</p>
      </div>
    </section>
  </div>
</body>
</html>
```